Fresh & Clean *NEW* BUSINESS CARD Needed - OPTOMETRY Clinic/Optical

High-tech optometry practice with 3 doctors seeking new business card.  We provide eye exams, sell, designer glasses/contacts/specialty eyewear and treat ocular diseases.  For our business cards, we are seeking fresh, clean, and crisp design as we grow our team (staffing change).  Simply adding doctors is making the card look busy/cluttered.
 Looking for professional, less cluttered look yet still have our logo, doctor names, phone, address, and website....If possible!  :)
Names:
Marisol Pettigrew, O.D.
Ray Bellamy, O.D.
Nora Vantreese, O.D.
Phone: 555-214-6038
Website: www.BrightLensStudio.example
Address:  418 Harlan P. Moody, Maple Hollow, KS 70000
Ultimately we have the main business card with all doctor sames and that card has two versions  (front is always the same).  The back has two designs (1) displays next appointment time/date, (2) for "general use" (non-appointment.)    I have attached what we have used in the past.  
We also need a design template for each team member in our practice with their name, title, and email.   Those should be designed with the "general use" back (see attached).
**Open to entirely new design so don't feel obligated to keep current format.  Need new perspective!  Also including our watermark and some other design features we have consistently used in past in our portfolio.  Included are two options for logos--vertical and horizontal.
**I also would like to remove "Member of Optic Guild" on our logo if possible**
 Other image files available upon request.

Target Market(s)

New patient & Current Patients

Industry/Entity Type

Optometry

Contact Information for Business Card

High-tech optometry practice with 3 doctors seeking new business card.  We provide eye exams, sell, designer glasses/contacts/specialty eyewear and treat ocular diseases.  For our business cards, we are seeking fresh, clean, and crisp design as we grow our team (staffing change).  Simply adding doctors is making the card look busy/cluttered.  Looking for professional, less cluttered look yet still have our logo, doctor names, phone, address, and website....If possible!  :) Names: Marisol Pettigrew, O.D. Ray Bellamy, O.D. Nora Vantreese, O.D. Phone: 555-214-6038 Website: www.BrightLensStudio.example Address:  418 Harlan P. Moody, Maple Hollow, KS 70000 Ultimately we have the main business card with all doctor sames and that card has two versions  (front is always the same).  The back has two designs (1) displays next appointment time/date, (2) for "general use" (non-appointment.)    I have attached what we have used in the past.   We also need a design template for each team member in our practice with their name, title, and email.   Those should be designed with the "general use" back (see attached). **Open to entirely new design so don't feel obligated to keep current format.  Need new perspective!  Also including our watermark and some other design features we have consistently used in past in our portfolio.  Included are two options for logos--vertical and horizontal. **I also would like to remove "Member of Optic Guild" on our logo if possible**  Other image files available upon request.

Font styles to use
Other font styles liked:
• We have used Montserrat / Yellowtail in the past

Colors

Designer to choose colors to be used in the design.

Requirements
Must have
• Clean & Fresh Design with Logo / Info provided in description. Horizontal orientation. **I have included the CMYK colors we currently have in our logo.
Should not have
• Cluttered

```html
<!DOCTYPE html>
<html lang="en">
<head>
<meta charset="utf-8">
<title>Bright Lens Studio – Business Card</title>
<link rel="stylesheet" href="https://fonts.googleapis.com/css2?family=Poppins:wght@300;400;600&display=swap">
<style>
  :root {
    --stage: #1c1c1c;
    --card-white: #ffffff;
    --card-grey: #6b6b6d;
    --pattern-grey: #5e5e60;
    --ice-blue: #b1dbe8;
    --ink: #6a6a6c;
    --ink-strong: #5a5a5c;
    --gold: #d6a81c;
  }
  * { margin: 0; padding: 0; box-sizing: border-box; }
  html, body {
    width: 1200px;
    height: 1015px;
    overflow: hidden;
    background: var(--stage);
    font-family: "Poppins", sans-serif;
  }
  .canvas { position: relative; width: 1200px; height: 1015px; }

  .card {
    position: absolute;
    width: 640px;
    height: 366px;
    overflow: hidden;
    box-shadow: 0 18px 40px rgba(0,0,0,0.55);
  }

  /* Back side */
  .card-back { left: 70px; top: 90px; }
  .card-back .pattern {
    position: absolute; inset: 0;
    background: radial-gradient(circle at 60% 40%, var(--card-grey), var(--pattern-grey));
  }
  .card-back .brand {
    position: absolute;
    right: 48px;
    bottom: 70px;
    display: flex;
    align-items: center;
    gap: 12px;
    color: var(--card-white);
    font-weight: 300;
    font-size: 32px;
    letter-spacing: 1px;
  }
  .brand-dot {
    width: 30px; height: 30px;
    border-radius: 50%;
    background: var(--card-white);
  }

  /* Front side */
  .card-front { left: 490px; top: 540px; background: var(--card-white); }
  .card-front .shape { position: absolute; inset: 0; }
  .card-front .brand-stack {
    position: absolute;
    left: 120px;
    top: 108px;
    width: 260px;
    text-align: center;
    color: var(--ink);
    font-weight: 300;
    font-size: 34px;
    line-height: 1.05;
  }
  .brand-stack .brand-dot {
    background: var(--ice-blue);
    width: 54px; height: 54px;
    margin: 0 auto 14px;
  }

  .info {
    position: absolute;
    left: 370px;
    top: 58px;
    color: var(--ink);
  }
  .doctor-name {
    font-weight: 600;
    font-size: 19px;
    color: var(--ink-strong);
    white-space: nowrap;
  }
  .doctor-name .title { color: var(--gold); font-weight: 400; }
  .personal { margin-top: 10px; font-size: 13px; font-weight: 300; line-height: 1.45; }
  .divider {
    width: 120px;
    height: 2px;
    background: var(--ice-blue);
    margin: 16px 0;
  }
  .contact-row {
    display: flex;
    align-items: center;
    gap: 10px;
    font-size: 13px;
    font-weight: 300;
    line-height: 1.6;
    white-space: nowrap;
  }
  .contact-icon {
    width: 18px; height: 18px;
    border-radius: 50%;
    background: var(--gold);
    display: flex; align-items: center; justify-content: center;
    flex: none;
  }
  .address { margin-top: 10px; font-size: 13px; font-weight: 300; line-height: 1.45; }
</style>
</head>
<body>
<main class="canvas">

  <section class="card card-back" aria-label="Business card back">
    <div class="pattern" role="img" aria-label="Faint repeating brand-mark pattern on grey"></div>
    <div class="brand">
      <span class="brand-dot"></span>
      <span class="brand-name">Bright Lens Studio</span>
    </div>
  </section>

  <section class="card card-front" aria-label="Business card front">
    <svg class="shape" viewBox="0 0 640 366" width="640" height="366" aria-hidden="true">
      <polygon points="0,0 170,0 230,60 230,306 270,366 0,366" fill="var(--ice-blue)"/>
      <circle cx="250" cy="190" r="148" fill="var(--card-white)"/>
    </svg>

    <div class="brand-stack">
      <div class="brand-dot"></div>
      <div>Bright Lens</div>
      <div>Studio</div>
    </div>

    <div class="info">
      <p class="doctor-name">Marisol Pettigrew, <span class="title">O.D.</span></p>
      <p class="personal">555-302-1184<br>hello@BrightLensStudio.example</p>
      <div class="divider"></div>
      <p class="contact-row">
        <span class="contact-icon">
          <svg width="10" height="10" viewBox="0 0 24 24" aria-hidden="true"><path fill="#fff" d="M6.6 10.8a15.1 15.1 0 0 0 6.6 6.6l2.2-2.2a1 1 0 0 1 1-.25 11.4 11.4 0 0 0 3.6.57 1 1 0 0 1 1 1V20a1 1 0 0 1-1 1A17 17 0 0 1 3 4a1 1 0 0 1 1-1h3.5a1 1 0 0 1 1 1c0 1.25.2 2.45.57 3.57a1 1 0 0 1-.25 1z"/></svg>
        </span>
        555-214-6038
      </p>
      <p class="contact-row">
        <span class="contact-icon">
          <svg width="11" height="11" viewBox="0 0 24 24" aria-hidden="true" fill="none" stroke="#fff" stroke-width="2"><circle cx="12" cy="12" r="9"/><path d="M3 12h18M12 3c3 3.5 3 14.5 0 18M12 3c-3 3.5-3 14.5 0 18"/></svg>
        </span>
        www.BrightLensStudio.example
      </p>
      <p class="address">418 Harlan P. Moody, Maple<br>Hollow, KS 70000</p>
    </div>
  </section>

</main>
</body>
</html>
```